Facebook Page Design for Manufacturing Company

Looking for a facebook page design for Torvale Inc that uses design queues from the website www.torvaleinc.example. Header update and possibly profile picture to coordinate with style and colors from website. Current header does not convey enough information, would like to use more action photos of machines working and better highlights of wording.
Industry/Entity Type
Manufacturing - Machining

```html
<!DOCTYPE html>
<html lang="en">
<head>
<meta charset="utf-8">
<title>Torvale Inc – Facebook Cover</title>
<link rel="stylesheet" href="https://fonts.googleapis.com/css2?family=Montserrat:wght@600;700;800&display=swap">
<style>
  :root {
    --brand-red: #b01e24;
    --ink: #1a1a1a;
    --paper: #ffffff;
    --backdrop: #e6e7ea;
    --photo-sky: #3b8fd0;
    --photo-steel: #8a8f96;
    --photo-warm: #b59a7a;
    --photo-mint: #cfe3e0;
  }
  html, body {
    margin: 0;
    width: 1067px;
    height: 1200px;
    overflow: hidden;
    background: var(--backdrop);
    font-family: "Montserrat", sans-serif;
  }
  .cover {
    position: absolute;
    left: 33px;
    top: 415px;
    width: 1000px;
    height: 370px;
    background: var(--paper);
    overflow: hidden;
    box-shadow: 0 6px 24px rgba(0,0,0,.12);
  }
  .cover__shapes {
    position: absolute;
    inset: 0;
    width: 100%;
    height: 100%;
  }
  .sectors {
    position: absolute;
    left: 46px;
    top: 76px;
    display: flex;
    gap: 26px;
    margin: 0;
    padding: 0;
    list-style: none;
    font-weight: 600;
    font-size: 15px;
    color: var(--ink);
  }
  .sectors li {
    display: flex;
    align-items: center;
    gap: 9px;
  }
  .sectors li::before {
    content: "";
    width: 11px;
    height: 11px;
    border-radius: 50%;
    background: var(--brand-red);
  }
  .brand {
    position: absolute;
    left: 76px;
    top: 112px;
    width: 480px;
    text-align: center;
    color: var(--brand-red);
    font-weight: 800;
    line-height: 1;
  }
  .brand__name {
    display: block;
    font-size: 80px;
    letter-spacing: -1px;
  }
  .brand__suffix {
    display: block;
    font-size: 36px;
    margin-top: 8px;
    letter-spacing: 1px;
  }
  .tagline {
    position: absolute;
    left: 36px;
    top: 268px;
    width: 560px;
    margin: 0;
    text-align: center;
    font-weight: 600;
    font-size: 14px;
    letter-spacing: .2px;
    color: var(--ink);
  }
</style>
</head>
<body>
  <section class="cover">
    <svg class="cover__shapes" viewBox="0 0 1250 463" preserveAspectRatio="none" aria-hidden="false">
      <defs>
        <pattern id="hatch" width="10" height="11" patternUnits="userSpaceOnUse" patternTransform="skewX(-35)">
          <rect width="5" height="11" fill="#b01e24"/>
        </pattern>
        <linearGradient id="g-care" x1="0" y1="0" x2="1" y2="1">
          <stop offset="0" stop-color="#eef2f3"/><stop offset="1" stop-color="#9fc9c0"/>
        </linearGradient>
        <linearGradient id="g-air" x1="0" y1="0" x2="0" y2="1">
          <stop offset="0" stop-color="#7b8c99"/><stop offset="1" stop-color="#6a4d2e"/>
        </linearGradient>
        <linearGradient id="g-grid" x1="0" y1="0" x2="0" y2="1">
          <stop offset="0" stop-color="#3b8fd0"/><stop offset="1" stop-color="#8cc6ee"/>
        </linearGradient>
        <linearGradient id="g-plant" x1="0" y1="0" x2="0" y2="1">
          <stop offset="0" stop-color="#9aa3ab"/><stop offset="1" stop-color="#7a6a55"/>
        </linearGradient>
      </defs>

      <!-- corner dots -->
      <g class="dots" fill="var(--brand-red)">
        <circle cx="24" cy="20" r="4"/><circle cx="39" cy="20" r="4"/><circle cx="54" cy="20" r="4"/>
        <circle cx="24" cy="34" r="4"/><circle cx="39" cy="34" r="4"/>
        <circle cx="24" cy="49" r="4"/>
      </g>

      <!-- hatched accents -->
      <rect class="hatch-top" x="455" y="27" width="140" height="11" fill="url(#hatch)"/>
      <rect class="hatch-bottom" x="552" y="428" width="140" height="11" fill="url(#hatch)"/>

      <!-- base bar -->
      <polygon class="base-bar" points="0,427 477,427 488,438 0,438" fill="var(--brand-red)"/>

      <!-- crossing bands -->
      <g class="cross" fill="var(--brand-red)">
        <polygon points="690,0 770,0 928,158 888,198"/>
        <polygon points="730,463 812,463 928,347 888,307"/>
        <polygon points="1180,0 1250,0 1250,20 1137,133 1097,93"/>
        <polygon points="1165,463 1240,463 1135,358 1097,396"/>
      </g>

      <!-- diamond frames -->
      <g class="frames" fill="var(--brand-red)">
        <polygon points="990,8 1082,100 990,192 898,100"/>
        <polygon points="1090,110 1188,208 1090,306 992,208"/>
        <polygon points="932,153 1026,247 932,341 838,247"/>
        <polygon points="1032,257 1126,351 1032,445 938,351"/>
      </g>

      <!-- photo slots -->
      <polygon role="img" aria-label="Hands cupping glowing medical icons" points="990,16 1074,100 990,184 906,100" fill="url(#g-care)" stroke="#fff" stroke-width="4"/>
      <polygon role="img" aria-label="Airliner taking off over a lit runway" points="1090,118 1180,208 1090,298 1000,208" fill="url(#g-air)" stroke="#fff" stroke-width="4"/>
      <polygon role="img" aria-label="Power transmission tower against blue sky" points="932,161 1018,247 932,333 846,247" fill="url(#g-grid)" stroke="#fff" stroke-width="4"/>
      <polygon role="img" aria-label="Industrial refinery plant at dusk" points="1032,265 1118,351 1032,437 946,351" fill="url(#g-plant)" stroke="#fff" stroke-width="4"/>
    </svg>

    <ul class="sectors">
      <li>Aerospace &amp; Defense</li>
      <li>Energy</li>
      <li>Medical Device</li>
      <li>Industrial</li>
    </ul>

    <h1 class="brand" aria-label="Torvale Inc">
      <span class="brand__name">TORVALE</span>
      <span class="brand__suffix">INC.</span>
    </h1>

    <p class="tagline">MAXIMUM VALUE WORLD CLASS QUALITY PRECISION MACHINING</p>
  </section>
</body>
</html>
```